Zorvik App Graphics Design

Our application promotes location based self expression via pictures and text. The primary focus of the application is on the content posted and not on the person that posted it.

We want a very clean and fresh design that evokes positive energy. Our site is unique so our design should be as well. People will reveal thoughts on our site, so the design should convey a "revealing" feel. Our site is a place where people are comfortable to freely express themselves. Colors we have in mind are blue and green hues with earth tones for background.

Our project is to design ten screens for our Zorvik application at resolution of 1136-by-640 pixels:

Feed Screen
Camera Screen
Post Screen
Check In Screen
Approval Screen
Map Screen
Flag Screen
Feed Select Screen
Export Screen
Menu Screen

In the contest phase we will require only three screens to be submitted. The screens we require to be submitted are: Feed Screen; Map Screen and Camera Screen. The designer we select as the winner of the competition will then complete the project and deliver a total of the ten screens described above in the handover phase.

We have attached a document below with detailed specs of each screen, we ask for your innovation to bring these screens to life through your design.
Updates

We want to clarify one aspect regarding the VISOR: the visor needs to be transparent so that when the picture scrolls underneath it, you can still see the picture underneath the visor.

Hi Everyone,

We have noticed that some designers need clarification regarding the visor element in the feed screen.
I have attached two examples to our brief area called:
Visor Example 1 and Visor Example 2

Please note that these are not the style we are looking for but are a good example to the concept of a Transparent Visor above the feed stream. We are looking for you guys to come up with a Visor concept that is consistent with the style of the design you are submitting.

Thanks,

Bo

Target Market(s)

People 17-40 who want to share their thought about the world around them.

Industry/Entity Type

Flag

Font styles to use
Sans Serif
Other font styles liked:
• We like “Helvetica New” or “Avenir” but are flexible

Requirements
Must have
• Visor component should look innovative.

```html
<!DOCTYPE html>
<html lang="en">
<head>
<meta charset="utf-8">
<title>Zorvik App Screens</title>
<link href="https://fonts.googleapis.com/css2?family=Arimo:wght@400;700&display=swap" rel="stylesheet">
<style>
:root{
  --page:#1c1c1c;
  --ink:#ffffff;
  --blue:#2e5590;
  --blue-hi:#4a74b2;
  --blue-lo:#223f6e;
  --bar-dark:#1a1f2c;
  --title-hi:#5a5a5a;
  --title-lo:#1e1e1e;
  --stat:#7d7d7d;
  --card:#d9d9d9;
  --card-ink:#222a3a;
  --green:#5cb85c;
  --map:#e6e2da;
  --callout:#f2f2f2;
}
*{box-sizing:border-box;margin:0;padding:0}
html,body{width:1200px;height:772px;overflow:hidden;background:var(--page);font-family:"Arimo",Arial,sans-serif;color:var(--ink)}
.screen{position:absolute;top:201px;width:247px;height:370px;overflow:hidden;background:#000}
.screen--feed{left:182px}
.screen--camera{left:477px}
.screen--map{left:772px}
.status{position:absolute;left:0;top:0;width:100%;height:15px;background:#000;font-size:9px;font-weight:700;display:flex;align-items:center;padding:0 4px}
.status .carrier{flex:1}
.status .clock{flex:1;text-align:center}
.status .battery{flex:1;text-align:right}
.navbar{position:absolute;top:15px;left:0;width:100%;height:35px;background:linear-gradient(var(--blue-hi),var(--blue-lo));display:flex}
.navbar .item{flex:1;display:flex;flex-direction:column;align-items:center;justify-content:center;font-size:8px;gap:2px}
.titleband{position:absolute;left:0;width:100%;background:linear-gradient(var(--title-hi),var(--title-lo));display:flex;align-items:center;justify-content:center;font-size:16px;font-weight:700;text-shadow:0 1px 2px #000}
.split{position:absolute;left:0;width:100%;display:flex;background:var(--blue);font-size:8px}
.split .half{flex:1;display:flex;align-items:center;justify-content:center;gap:4px}
.split .half+.half{border-left:1px solid #fff}
.photo{position:absolute;left:0;width:100%}
.photo--building{top:112px;height:120px;background:linear-gradient(#f4f4f4 0%,#d8dcdc 45%,#7d8a8c 80%,#50595a)}
.photo--cafe{top:90px;height:193px;background:linear-gradient(160deg,#3b1d10,#a8612a 45%,#e3b070 70%,#6a3a1c)}
.stats{position:absolute;top:232px;left:0;width:100%;height:18px;background:var(--stat);display:flex;font-size:8px}
.stats .cell{flex:1;display:flex;align-items:center;justify-content:center;gap:4px}
.stats .cell+.cell{border-left:1px solid #ddd}
.infocard{position:absolute;top:272px;left:0;width:100%;height:41px;background:var(--card);color:var(--card-ink);padding:13px 19px 0;font-size:6px}
.infocard .place{font-weight:700;font-size:7px;margin-bottom:3px}
.nextbar{position:absolute;top:313px;left:0;width:100%;height:25px;background:var(--blue);display:flex;align-items:center;justify-content:center;gap:6px;font-size:10px}
.tabbar{position:absolute;top:338px;left:0;width:100%;height:32px;background:linear-gradient(#3a4254,var(--bar-dark));display:flex;font-size:7px}
.tabbar .tab{flex:1;display:flex;flex-direction:column;align-items:center;justify-content:center;gap:2px}
.tabbar--split .tab+.tab{border-left:1px solid #556}
.filters{position:absolute;top:283px;left:0;width:100%;height:55px;background:#8c8c8c;display:flex;justify-content:space-around;padding-top:4px}
.filter{width:55px;display:flex;flex-direction:column}
.filter .thumb{height:40px;border:1px solid #fff}
.filter .label{height:10px;background:#222;font-size:7px;display:flex;align-items:center;justify-content:center}
.thumb--vivid{background:linear-gradient(#4b2414,#c27634)}
.thumb--ansel{background:linear-gradient(#6a3046,#e6a0b0)}
.thumb--instant{background:linear-gradient(#3e3020,#b88e5c)}
.thumb--pro{background:linear-gradient(#5a4a40,#d8c0a8)}
.brand{position:absolute;top:14px;left:8px;font-size:20px;font-weight:700;letter-spacing:1px}
.places{position:absolute;top:15px;left:0;width:100%}
.place-row{height:22.5px;background:var(--blue);border-bottom:1px solid #1b3360;display:flex;align-items:center;padding:0 6px;font-size:7px;gap:12px}
.place-row .name{flex:1}
.map{position:absolute;top:82px;left:0;width:100%;height:288px;background:linear-gradient(135deg,var(--map),#d9d5cc)}
.zoom{position:absolute;top:8px;left:7px}
.compass{position:absolute;top:50px;left:99px}
.callout{position:absolute;top:100px;left:30px;width:196px;height:36px;background:var(--callout);display:flex;color:#222}
.callout .eta{width:43px;background:var(--green);color:#fff;font-size:8px;display:flex;flex-direction:column;align-items:center;justify-content:center;gap:2px}
.callout .text{padding:5px 5px;font-size:7px}
.callout .heading{font-size:11px;font-weight:700;margin-bottom:4px}
.marker{position:absolute;top:140px;left:218px}
.map-buttons{position:absolute;top:263px;left:60px;display:flex;gap:8px}
.map-btn{height:16px;border-radius:8px;background:linear-gradient(var(--blue-hi),var(--blue-lo));border:1px solid #9ab;font-size:6px;display:flex;align-items:center;justify-content:center;gap:4px;padding:0 8px}
</style>
</head>
<body>

<!-- Feed screen -->
<section class="screen screen--feed">
  <div class="status"><span class="carrier">Telvo NL</span><span class="clock">08:39</span><span class="battery">100%</span></div>
  <nav class="navbar">
    <div class="item"><svg width="9" height="9"><g fill="#fff"><rect width="3" height="3"/><rect x="6" width="3" height="3"/><rect y="6" width="3" height="3"/><rect x="6" y="6" width="3" height="3"/></g></svg>Menu</div>
    <div class="item"><svg width="10" height="10"><circle cx="5" cy="5" r="5" fill="#fff"/></svg>Feed</div>
    <div class="item"><svg width="10" height="10"><circle cx="4" cy="4" r="3" fill="none" stroke="#fff" stroke-width="1.3"/><line x1="6" y1="6" x2="9.5" y2="9.5" stroke="#fff" stroke-width="1.5"/></svg>Search</div>
  </nav>
  <header class="titleband" style="top:50px;height:42px">My App Phone</header>
  <div class="split" style="top:92px;height:20px">
    <div class="half"><svg width="7" height="8"><path d="M1 0v8M1 0h6l-1.5 2 1.5 2H1" fill="#fff" stroke="#fff"/></svg>Flag</div>
    <div class="half"><svg width="8" height="8"><rect y="2" width="6" height="6" fill="#fff"/><path d="M4 4l4-4" stroke="#fff"/></svg>Export</div>
  </div>
  <div class="photo photo--building" role="img" aria-label="Photo of a modern shopping mall facade"></div>
  <div class="stats">
    <div class="cell"><svg width="8" height="8"><line x1="0" y1="8" x2="8" y2="0" stroke="#fff" stroke-width="1.3"/></svg>26 Mi</div>
    <div class="cell">5 Post</div>
    <div class="cell"><svg width="8" height="8"><circle cx="4" cy="4" r="3.3" fill="none" stroke="#fff"/></svg>30 min</div>
  </div>
  <div class="split" style="top:250px;height:22px">
    <div class="half"><svg width="9" height="9"><circle cx="4.5" cy="4.5" r="4.5" fill="#fff"/></svg>PROMOTE</div>
    <div class="half"><svg width="9" height="9"><circle cx="4.5" cy="4.5" r="4.5" fill="#fff"/><path d="M3 3l3 3M6 3L3 6" stroke="#2e5590"/></svg>DEMOTE</div>
  </div>
  <div class="infocard">
    <p class="place">Plaza Meridian</p>
    <p>Jl. Kenari Raya No. 12, Cendana, Kota Lama, Jakarta Pusat</p>
  </div>
  <div class="nextbar">Next Picture <svg width="12" height="12"><circle cx="6" cy="6" r="6" fill="#fff"/><path d="M5 3.5l2.5 2.5L5 8.5" stroke="#2e5590" stroke-width="1.5" fill="none"/></svg></div>
  <div class="tabbar tabbar--split">
    <div class="tab"><svg width="11" height="9"><rect y="1" width="11" height="8" rx="2" fill="#fff"/><circle cx="5.5" cy="5" r="2" fill="#1a1f2c"/></svg>Camera</div>
    <div class="tab"><svg width="10" height="10"><circle cx="5" cy="5" r="5" fill="#fff"/><path d="M2.5 5l2 2 3-4" stroke="#1a1f2c" fill="none" stroke-width="1.3"/></svg>Badge</div>
  </div>
</section>

<!-- Camera screen -->
<section class="screen screen--camera">
  <div class="status"><span class="carrier">Telvo NL</span><span class="clock">08:39</span><span class="battery">100%</span></div>
  <nav class="navbar">
    <div class="item"><svg width="11" height="11"><circle cx="5.5" cy="5.5" r="5" fill="none" stroke="#fff"/><path d="M6 2L4 6h2.5L5 9" stroke="#fff" fill="none"/></svg>Flash</div>
    <div class="item"><svg width="11" height="11"><circle cx="5.5" cy="5.5" r="5" fill="#fff"/></svg>Rotate</div>
    <div class="item"><svg width="11" height="11"><circle cx="5.5" cy="5.5" r="4.5" fill="none" stroke="#fff"/><circle cx="5.5" cy="5.5" r="1.5" fill="#fff"/></svg>Focus</div>
    <div class="item"><svg width="9" height="9"><path d="M1 1l7 7M8 1L1 8" stroke="#fff" stroke-width="1.4"/></svg>Cancel</div>
  </nav>
  <header class="titleband" style="top:50px;height:40px">My App Phone</header>
  <div class="photo photo--cafe" role="img" aria-label="Photo of a bakery cafe counter with warm interior lighting">
    <span class="brand">CRUMBLINE</span>
  </div>
  <div class="filters">
    <div class="filter"><div class="thumb thumb--vivid" role="img" aria-label="Vivid filter preview"></div><div class="label">Vivid</div></div>
    <div class="filter"><div class="thumb thumb--ansel" role="img" aria-label="Ansel filter preview"></div><div class="label">Ansel</div></div>
    <div class="filter"><div class="thumb thumb--instant" role="img" aria-label="Instant filter preview"></div><div class="label">Instant</div></div>
    <div class="filter"><div class="thumb thumb--pro" role="img" aria-label="Pro filter preview"></div><div class="label">Pro</div></div>
  </div>
  <div class="tabbar">
    <div class="tab"><svg width="10" height="12"><rect width="10" height="12" rx="2" fill="#fff"/><circle cx="5" cy="7" r="2" fill="#1a1f2c"/></svg>Retake</div>
    <div class="tab"><svg width="12" height="12"><circle cx="6" cy="6" r="3" fill="#fff"/><path d="M6 0v2M6 10v2M0 6h2M10 6h2" stroke="#fff"/></svg>Brightness</div>
    <div class="tab"><svg width="12" height="10"><rect y="1" width="12" height="9" rx="2" fill="#fff"/><circle cx="6" cy="5.5" r="2.3" fill="#1a1f2c"/></svg>Take Photo</div>
    <div class="tab"><svg width="11" height="11"><path d="M2.5 0v8.5H11M0 2.5h8.5V11" stroke="#fff" fill="none" stroke-width="1.4"/></svg>Crop</div>
    <div class="tab"><svg width="12" height="12"><circle cx="6" cy="6" r="4" fill="#fff"/><path d="M6 0v12M0 6h12" stroke="#fff"/></svg>Effect</div>
  </div>
</section>

<!-- Map screen -->
<section class="screen screen--map">
  <div class="status"><span class="carrier">Telvo NL</span><span class="clock">08:39</span><span class="battery">100%</span></div>
  <div class="places">
    <div class="place-row"><svg width="11" height="11"><path d="M2 9l3-3M4 2l5 5M5 1l5 5-3 1-3-3z" stroke="#fff" fill="#fff"/></svg><span class="name">Hotel Lintang</span><svg width="11" height="11"><circle cx="5.5" cy="5.5" r="5.5" fill="#fff"/><path d="M4.5 3l2.5 2.5L4.5 8" stroke="#2e5590" stroke-width="1.4" fill="none"/></svg></div>
    <div class="place-row"><svg width="11" height="11"><path d="M2 9l3-3M4 2l5 5M5 1l5 5-3 1-3-3z" stroke="#fff" fill="#fff"/></svg><span class="name">Cahaya City</span><svg width="11" height="11"><circle cx="5.5" cy="5.5" r="5.5" fill="#fff"/><path d="M4.5 3l2.5 2.5L4.5 8" stroke="#2e5590" stroke-width="1.4" fill="none"/></svg></div>
    <div class="place-row"><svg width="11" height="11"><path d="M2 9l3-3M4 2l5 5M5 1l5 5-3 1-3-3z" stroke="#fff" fill="#fff"/></svg><span class="name">Arena Bintang Stadium</span><svg width="11" height="11"><circle cx="5.5" cy="5.5" r="5.5" fill="#fff"/><path d="M4.5 3l2.5 2.5L4.5 8" stroke="#2e5590" stroke-width="1.4" fill="none"/></svg></div>
  </div>
  <div class="map" role="img" aria-label="Street map of a central city district around the dropped pin">
    <svg class="zoom" width="26" height="180"><circle cx="13" cy="13" r="12" fill="#f4f4f4" stroke="#999"/><path d="M13 5l-2 3h4zM13 21l-2-3h4zM5 13l3-2v4zM21 13l-3-2v4z" fill="#777"/><rect x="9" y="60" width="8" height="110" fill="#f4f4f4" stroke="#999"/><rect x="10" y="62" width="6" height="14" fill="#e49a2e"/></svg>
    <svg class="compass" width="46" height="46"><circle cx="23" cy="23" r="20" fill="none" stroke="#111" stroke-width="2"/><line x1="19" y1="8" x2="19" y2="38" stroke="#111" stroke-width="2.5"/><line x1="27" y1="8" x2="27" y2="38" stroke="#2f8fd8" stroke-width="2.5"/></svg>
    <div class="callout">
      <div class="eta"><svg width="20" height="12"><path d="M2 6l3-5h10l3 5v5H2z" fill="#fff"/><circle cx="6" cy="11" r="1.5" fill="#5cb85c"/><circle cx="14" cy="11" r="1.5" fill="#5cb85c"/></svg>35 min</div>
      <div class="text"><p class="heading">Dropped Pin</p><p>Jl. Kenari Raya No. 12, Cendana.....</p></div>
    </div>
    <svg class="marker" width="10" height="16"><path d="M5 16L1 7a4 4 0 1 1 8 0z" fill="#d9473b"/><circle cx="5" cy="5" r="1.5" fill="#8a1f18"/></svg>
    <div class="map-buttons">
      <div class="map-btn"><svg width="9" height="9"><circle cx="4.5" cy="4.5" r="4.5" fill="#fff"/><path d="M2.2 4.5l1.6 1.6L6.8 3" stroke="#2e5590" fill="none" stroke-width="1.2"/></svg>Done</div>
      <div class="map-btn">Current Location</div>
    </div>
  </div>
</section>

</body>
</html>
```